Bramble Systems Voip Broucher

We require a full page broucher 8.5X11 format for a Voip promotion
Updates

Target Market(s)

Business Customer

Industry/Entity Type

Voip

Colors
ec1f27
0592cd

Requirements
Must have
• Logo, Information as provided, our phone number 1-877-555-0193, Colors that match the logo. Reds, blues and white please.

```html
<!DOCTYPE html>
<html lang="en">
<head>
<meta charset="utf-8">
<title>Bramble Systems VoIP Brochure</title>
<link href="https://fonts.googleapis.com/css2?family=Bebas+Neue&family=Raleway:wght@300;400;600;700&display=swap" rel="stylesheet">
<style>
  :root{
    --red:#ec1f27;
    --red-light:#f2555b;
    --blue:#0592cd;
    --blue-bright:#29a8e0;
    --blue-light:#3fb6e8;
    --ink:#3a3a3a;
    --charcoal:#3b3b3c;
    --brand:#8a1c22;
    --white:#ffffff;
    --stage:#ececec;
  }
  *{margin:0;padding:0;box-sizing:border-box}
  html,body{width:1200px;height:1200px;overflow:hidden}
  body{background:var(--stage);font-family:'Raleway',sans-serif;position:relative}
  .page{position:absolute;top:250px;width:679px;height:879px;background:var(--white);
        transform:scale(0.8);transform-origin:0 0;overflow:hidden;color:var(--ink)}
  .page--front{left:46px}
  .page--back{left:612px}
  .page svg.shapes{position:absolute;left:0;top:0}
  .abs{position:absolute}
  .condensed{font-family:'Bebas Neue',sans-serif;font-weight:400;letter-spacing:.2px}

  .contact{font-size:25px;color:#555;display:flex;align-items:center;gap:8px;font-weight:400}
  .contact svg{width:14px;height:22px}
  .contact-caption{font-size:17px;color:#444;text-transform:uppercase;font-weight:400}

  .brand-name{display:flex;align-items:center;gap:10px;color:var(--brand);
              font-weight:700;font-size:30px;text-transform:uppercase;letter-spacing:1px;line-height:1}
  .brand-name .mark{width:18px;height:18px;background:var(--brand)}

  .headline{left:52px;top:212px;color:var(--white);font-size:29px;line-height:33px;font-weight:300}
  .headline strong{font-weight:700}
  .cost-q{left:52px;top:374px;color:var(--white);font-size:20px;font-weight:300}
  .fee{left:52px;top:414px;color:var(--blue-bright);font-size:26px;line-height:27px}

  .example-title{left:54px;top:536px;color:var(--white);font-size:29px;line-height:27px}
  .example-text{left:56px;top:616px;width:200px;color:var(--white);font-size:14.5px;line-height:18px;font-weight:400}
  .example-calc{left:56px;top:726px;color:var(--white);font-size:17.5px;line-height:21px}
  .example-total{left:58px;top:774px;color:var(--white);font-size:42px;line-height:40px}
  .example-unit{left:58px;top:812px;color:var(--white);font-size:17px}

  .get-title{left:318px;top:602px;font-size:19px;color:#444;font-weight:400}
  .benefits{left:316px;top:636px;list-style:none;width:330px}
  .benefits li{display:flex;gap:18px;align-items:flex-start;margin-bottom:14px}
  .benefits .num{font-size:54px;line-height:48px;color:var(--blue);font-weight:300;width:30px}
  .benefits p{font-size:17px;line-height:20px;color:#333;padding-top:4px}

  .features-title{left:47px;top:136px;color:var(--blue-bright);font-size:33px}
  .feature{position:absolute;width:110px;text-align:center;color:var(--white);font-size:15px;line-height:14px;font-weight:400}
  .feature .icon{width:46px;height:46px;border-radius:50%;background:var(--white);margin:0 auto 10px;display:flex;align-items:center;justify-content:center}
  .feature .icon svg{width:26px;height:26px}
  .support-title{left:47px;top:374px;color:var(--blue-bright);font-size:33px}
  .support-list{left:48px;top:416px;color:var(--white);font-size:17.5px;display:flex;gap:10px;list-style:none}
  .support-list li::before{content:"• "}

  .qa-label{left:50px;top:456px;width:86px;height:29px;background:var(--red);color:var(--white);
            font-size:25px;font-weight:600;line-height:29px;text-align:center}
  .qa{left:50px;top:498px;width:605px;color:var(--white);font-size:13px;line-height:15.5px}
  .qa dt{font-weight:600}
  .qa dd{margin-bottom:8px;font-weight:400}
</style>
</head>
<body>

<!-- FRONT -->
<section class="page page--front">
  <svg class="shapes" width="679" height="879" viewBox="0 0 679 879">
    <polygon points="0,0 70,0 0,158" fill="var(--red)"/>
    <rect x="0" y="178" width="679" height="335" fill="#3a3a3a"/>
    <polygon points="0,178 400,178 530,513 0,513" fill="url(#officeShade)" role="img" aria-label="Photo of a modern office interior with city windows"/>
    <polygon points="400,178 679,178 679,513 540,513" fill="var(--red)"/>
    <polygon points="242,178 272,116 296,178" fill="var(--blue-light)"/>
    <polygon points="272,116 362,116 500,470 410,470" fill="var(--blue)"/>
    <polygon points="0,513 327,513 167,879 0,879" fill="var(--blue-bright)"/>
    <defs>
      <linearGradient id="officeShade" x1="0" y1="0" x2="1" y2="1">
        <stop offset="0" stop-color="#2e2f31"/>
        <stop offset=".55" stop-color="#4a4b4d"/>
        <stop offset="1" stop-color="#2a2a2b"/>
      </linearGradient>
      <linearGradient id="deskPhone" x1="0" y1="0" x2="1" y2="1">
        <stop offset="0" stop-color="#2b2b2d"/>
        <stop offset="1" stop-color="#0e0e10"/>
      </linearGradient>
    </defs>
    <rect x="332" y="278" width="310" height="305" rx="14" fill="url(#deskPhone)" role="img" aria-label="Photo of a black VoIP desk phone with colour touchscreen"/>
  </svg>

  <div class="abs" style="left:74px;top:48px">
    <div class="contact">
      <svg viewBox="0 0 14 22"><rect x="1.5" y="1" width="11" height="20" rx="2" fill="none" stroke="var(--blue)" stroke-width="2"/><rect x="5" y="17" width="4" height="1.6" fill="var(--blue)"/></svg>
      1-877-555-0193
    </div>
    <div class="contact-caption">Bramble Systems Group</div>
  </div>
  <div class="abs brand-name" style="left:330px;top:62px"><span class="mark"></span>Bramble Systems</div>

  <h1 class="abs headline">Upgrade your<br>office phone system<br><strong>and cut your<br>phone bill in half</strong></h1>
  <p class="abs cost-q">What does it cost?</p>
  <p class="abs fee condensed">Flat monthly fee of $25.00<br>per month per desk phone</p>

  <h2 class="abs example-title condensed">Costing for a<br>hypothetical example:</h2>
  <p class="abs example-text">Harbor Administration office has 35 office phones. What will it cost to upgrade the office and what will the monthly cost be?</p>
  <p class="abs example-calc">$25.00 line fee x<br>35 handsets =</p>
  <p class="abs example-total condensed">$875.00</p>
  <p class="abs example-unit condensed">Per month.</p>

  <h3 class="abs get-title">WHAT DO YOU GET?</h3>
  <ol class="abs benefits">
    <li><span class="num">1</span><p>Modern Office phone system with the latest features only available through Voice over IP</p></li>
    <li><span class="num">2</span><p>Installation and ongoing support services as required</p></li>
    <li><span class="num">3</span><p>Unlimited local and long distance calling within North America only</p></li>
  </ol>
</section>

<!-- BACK -->
<section class="page page--back">
  <svg class="shapes" width="679" height="879" viewBox="0 0 679 879">
    <defs>
      <linearGradient id="officeShade2" x1="0" y1="0" x2="1" y2="1">
        <stop offset="0" stop-color="#2c2d2f"/>
        <stop offset=".5" stop-color="#55575a"/>
        <stop offset="1" stop-color="#2b2b2c"/>
      </linearGradient>
    </defs>
    <rect x="0" y="115" width="679" height="358" fill="var(--charcoal)"/>
    <polygon points="476,115 679,115 679,473 650,473" fill="url(#officeShade2)" role="img" aria-label="Photo of an office with large city-view windows"/>
    <polygon points="268,115 303,35 340,115" fill="var(--red-light)"/>
    <polygon points="303,35 440,35 635,473 500,473" fill="var(--red)"/>
    <polygon points="48,473 679,473 679,760 625,879 0,879 0,580" fill="var(--blue-bright)"/>
  </svg>

  <div class="abs brand-name" style="left:50px;top:50px;font-size:24px"><span class="mark" style="width:15px;height:15px"></span>Bramble Systems</div>
  <div class="abs contact" style="left:494px;top:50px;font-size:21px">
    <svg viewBox="0 0 14 22"><rect x="1.5" y="1" width="11" height="20" rx="2" fill="none" stroke="var(--blue)" stroke-width="2"/><rect x="5" y="17" width="4" height="1.6" fill="var(--blue)"/></svg>
    1-877-555-0193
  </div>

  <h2 class="abs features-title condensed">Included phone feature set:</h2>

  <div class="feature" style="left:25px;top:189px"><div class="icon"><svg viewBox="0 0 24 24"><path d="M6 3l3 0 1.5 4-2 1.5a11 11 0 0 0 6 6l1.5-2 4 1.5v3a2 2 0 0 1-2 2A16 16 0 0 1 4 5a2 2 0 0 1 2-2z" fill="var(--blue)"/></svg></div>Auto<br>attendant</div>
  <div class="feature" style="left:127px;top:189px"><div class="icon"><svg viewBox="0 0 24 24"><circle cx="6.5" cy="12" r="4" fill="none" stroke="var(--blue)" stroke-width="2"/><circle cx="17.5" cy="12" r="4" fill="none" stroke="var(--blue)" stroke-width="2"/><line x1="6.5" y1="16" x2="17.5" y2="16" stroke="var(--blue)" stroke-width="2"/></svg></div>Voicemail</div>
  <div class="feature" style="left:226px;top:189px"><div class="icon"><svg viewBox="0 0 24 24"><path d="M3 6l7 8 4-5 7 7" fill="none" stroke="var(--blue)" stroke-width="2"/><path d="M15 4h6v6" fill="none" stroke="var(--blue)" stroke-width="2"/><line x1="21" y1="4" x2="14" y2="11" stroke="var(--blue)" stroke-width="2"/></svg></div>3 ways calling</div>

  <div class="feature" style="left:25px;top:284px"><div class="icon"><svg viewBox="0 0 24 24"><path d="M5 4l3 0 1.5 4-2 1.5a11 11 0 0 0 6 6l1.5-2 4 1.5v3a2 2 0 0 1-2 2A16 16 0 0 1 3 6a2 2 0 0 1 2-2z" fill="var(--blue)"/><path d="M15 3a6 6 0 0 1 6 6M15 7a2 2 0 0 1 2 2" fill="none" stroke="var(--blue)" stroke-width="1.6"/></svg></div>hands free</div>
  <div class="feature" style="left:127px;top:284px"><div class="icon"><svg viewBox="0 0 24 24"><path d="M5 8l3 0 1.5 4-2 1.5a9 9 0 0 0 5 5l1.5-2 4 1.5v3H16A14 14 0 0 1 3 10a2 2 0 0 1 2-2z" fill="var(--blue)"/><path d="M12 8l8-5M15 3h5v5" fill="none" stroke="var(--blue)" stroke-width="2"/></svg></div>call forward</div>
  <div class="feature" style="left:226px;top:284px"><div class="icon"><svg viewBox="0 0 24 24"><g stroke="var(--blue)" stroke-width="2"><line x1="5" y1="8" x2="5" y2="16"/><line x1="9" y1="5" x2="9" y2="19"/><line x1="13" y1="4" x2="13" y2="20"/><line x1="17" y1="6" x2="17" y2="18"/><line x1="20" y1="9" x2="20" y2="15"/></g></svg></div>Intercom</div>
  <div class="feature" style="left:320px;top:284px"><div class="icon"><svg viewBox="0 0 24 24"><rect x="3" y="6" width="18" height="12" fill="var(--blue)"/><path d="M3 6l9 7 9-7" fill="none" stroke="var(--white)" stroke-width="1.5"/></svg></div>email tie in</div>

  <h2 class="abs support-title condensed">Support services</h2>
  <ul class="abs support-list">
    <li>Hardware installation</li><li>Training</li><li>Ongoing support</li>
  </ul>

  <div class="abs qa-label">Q &amp; A</div>
  <dl class="abs qa">
    <dt>Q How does it work?</dt>
    <dd>A Rather than calls coming and going through Northline phone lines, calls get routed to the exchange through the internet connection.</dd>
    <dt>Q Is this a new and is it reliable</dt>
    <dd>A This technology has been around for over a decade. Its works very well and is used across the globe.</dd>
    <dt>Q Can I keep our offices existing telephone number?</dt>
    <dd>A Yes, we can port the existing number</dd>
    <dt>Q Is there 911 services</dt>
    <dd>A Yes, we register your legal land description with E911 and 911 calling is available</dd>
    <dt>Q Can we fax using VoIP</dt>
    <dd>A Yes faxing works fine through VoIP.</dd>
    <dt>Q How does it work?</dt>
    <dd>A Rather than calls coming and going through Northline phone lines, calls get routed to the exchange through the internet connection.</dd>
    <dt>Q What costs are not included to get the new phone system in place.</dt>
    <dd>A The new phone system run through ethernet office network cabling. Your office may need the cabling upgraded to allow use of VoIP phones. We can provide an affordable estimate to improve your cabling to support a VoIP phone.<br>A The calls will route through your existing office internet connection</dd>
  </dl>
</section>

</body>
</html>
```